Bubble map/flip book

I need someone to create a bubble map with explanations using the attached. This will be used to create a color coded flip book/manual. I need you to clean this up.

Dorothywinslade@postlark.com

```html
<!DOCTYPE html>
<html lang="en">
<head>
<meta charset="utf-8">
<title>Claim Denial Flip Book</title>
<link href="https://fonts.googleapis.com/css2?family=Open+Sans:wght@400;600;700&family=Arimo:wght@400;700&display=swap" rel="stylesheet">
<style>
:root{
  --stage:#8a8a8a;
  --paper:#ffffff;
  --ink:#111111;
  --header-dark:#2b2a2b;
  --yellow:#ffd400;
  --yellow-dark:#a38a00;
  --orange:#ffad00;
  --green:#5a9a3a;
  --purple:#55229a;
  --red-orange:#ee4422;
  --pink:#ea1e73;
  --pink-dark:#9c1449;
  --red:#dd0033;
  --brown:#8e6218;
  --blue:#1e3590;
}
*{box-sizing:border-box;margin:0;padding:0}
html,body{width:1200px;height:1045px;overflow:hidden;background:var(--stage)}
.canvas{position:relative;width:1200px;height:1045px;background:var(--stage)}
.page{position:absolute;width:365px;height:472px;background:var(--paper);overflow:hidden;font-family:"Arimo",sans-serif}
.texture{position:absolute;inset:0;background:linear-gradient(170deg,rgba(0,0,0,0.04) 0%,rgba(255,255,255,0) 25%,rgba(255,255,255,0) 55%,rgba(0,0,0,0.07) 100%)}
.page > *:not(.texture){position:absolute}
.connectors{left:0;top:0;width:365px;height:472px}
.header{left:24px;top:71px;width:317px;height:54px;display:flex;flex-direction:column;align-items:center;justify-content:center;font-family:"Open Sans",sans-serif;border-radius:2px}
.header--dark{background:var(--header-dark);color:#fff;font-weight:600;font-size:19px;letter-spacing:-0.2px;border-bottom:4px solid #000}
.header--yellow{background:var(--yellow);color:var(--ink);font-weight:600;font-size:13.5px;border-bottom:6px solid var(--yellow-dark)}
.header--pink{background:var(--pink);color:#fff;border-bottom:6px solid var(--pink-dark);line-height:1.25}
.header--pink strong{font-weight:700;font-size:14px}
.header--pink span{font-size:14px}
.box{display:flex;flex-direction:column;align-items:center;justify-content:center;text-align:center;color:#fff;font-size:8.5px;line-height:1.35;padding:4px}
.box--tall{justify-content:flex-start;padding-top:14px}
.category{width:69px;height:67px}
.flow{font-size:6.3px;line-height:1.3;border-radius:3px;padding:4px 5px}
.flow--top{justify-content:flex-start;padding-top:10px}
.flow--small{font-size:5.6px;justify-content:flex-start;padding-top:14px}
.ink{color:var(--ink)}
.contact{left:98px;top:142px;width:168px;height:44px;border-radius:3px;font-size:10px}
.contact em{font-size:7px;font-style:italic}
.page-title{left:0;width:365px;top:76px;text-align:center;font-family:"Open Sans",sans-serif;font-weight:600;font-size:15px}
.title-bar{left:58px;top:101px;width:248px;height:6px}
.notes{font-family:"Open Sans",sans-serif;font-size:5.3px;line-height:1.5;color:var(--ink)}
.notes ol{padding-left:9px}
.notes b{font-weight:700}
.corner{right:14px;bottom:8px;width:46px;height:38px}
</style>
</head>
<body>
<div class="canvas">

  <!-- Overview -->
  <section class="page" style="left:41px;top:42px">
    <div class="texture" role="img" aria-label="Faint grey geometric background"></div>
    <div class="header header--dark">CLAIM HAS BEEN DENIED</div>
    <svg class="connectors" viewBox="0 0 365 472">
      <g stroke-width="1">
        <line x1="49" y1="123" x2="49" y2="242" stroke="var(--yellow)"/>
        <line x1="94" y1="123" x2="94" y2="330" stroke="var(--pink)"/>
        <line x1="138" y1="123" x2="138" y2="242" stroke="var(--green)"/>
        <line x1="184" y1="123" x2="184" y2="330" stroke="var(--brown)"/>
        <line x1="227" y1="123" x2="227" y2="242" stroke="var(--purple)"/>
        <line x1="273" y1="123" x2="273" y2="330" stroke="var(--blue)"/>
        <line x1="316" y1="123" x2="316" y2="242" stroke="var(--red-orange)"/>
      </g>
      <g stroke="#fff" stroke-width="1">
        <circle cx="49" cy="123" r="2.5" fill="var(--yellow)"/>
        <circle cx="94" cy="123" r="2.5" fill="var(--pink)"/>
        <circle cx="138" cy="123" r="2.5" fill="var(--green)"/>
        <circle cx="184" cy="123" r="2.5" fill="var(--brown)"/>
        <circle cx="227" cy="123" r="2.5" fill="var(--purple)"/>
        <circle cx="273" cy="123" r="2.5" fill="var(--blue)"/>
        <circle cx="316" cy="123" r="2.5" fill="var(--red-orange)"/>
      </g>
      <g>
        <circle cx="49" cy="241" r="2" fill="var(--yellow)"/>
        <circle cx="94" cy="329" r="2" fill="var(--pink)"/>
        <circle cx="138" cy="241" r="2" fill="var(--green)"/>
        <circle cx="184" cy="329" r="2" fill="var(--brown)"/>
        <circle cx="227" cy="241" r="2" fill="var(--purple)"/>
        <circle cx="273" cy="329" r="2" fill="var(--blue)"/>
        <circle cx="316" cy="241" r="2" fill="var(--red-orange)"/>
      </g>
    </svg>
    <div class="box category box--tall" style="left:14px;top:242px;background:var(--yellow)">Authorization/<br>Referral<br>Needed</div>
    <div class="box category box--tall" style="left:104px;top:242px;background:var(--green)">Duplicate</div>
    <div class="box category box--tall" style="left:193px;top:242px;background:var(--purple)">Global<br>Inclusive</div>
    <div class="box category box--tall" style="left:282px;top:242px;background:var(--red-orange)">Post Timely<br>Filing</div>
    <div class="box category box--tall" style="left:61px;top:330px;background:var(--pink)">Coding/<br>Billing<br>Issues</div>
    <div class="box category box--tall" style="left:150px;top:330px;background:var(--brown)">Non-<br>Covered<br>Charge</div>
    <div class="box category box--tall" style="left:238px;top:330px;background:var(--blue)">Additional<br>Information<br>Requested</div>
  </section>

  <!-- Authorization flow -->
  <section class="page" style="left:418px;top:42px">
    <div class="texture" role="img" aria-label="Faint grey geometric background"></div>
    <div class="header header--yellow">Claim denied for no authorization/referral.</div>
    <div class="box contact ink" style="background:var(--yellow)">Contact carrier.<em>Was claim processed in network or out of network?</em></div>
    <svg class="connectors" viewBox="0 0 365 472" fill="none">
      <g stroke="var(--yellow)" stroke-width="1">
        <polyline points="182,186 182,196"/>
        <polyline points="68,212 68,196 297,196 297,212"/>
      </g>
      <g fill="var(--yellow)">
        <path d="M65,209 L71,209 L68,214 Z"/><path d="M294,209 L300,209 L297,214 Z" fill="var(--orange)"/>
      </g>
      <g stroke="var(--yellow)" stroke-width="1.3"><line x1="50" y1="298" x2="50" y2="332"/><line x1="131" y1="298" x2="131" y2="332"/></g>
      <g stroke="var(--orange)" stroke-width="1.3"><line x1="243" y1="298" x2="243" y2="332"/><line x1="323" y1="298" x2="323" y2="332"/></g>
      <path d="M46,328 L54,328 L50,336 Z M127,328 L135,328 L131,336 Z" fill="var(--yellow)"/>
      <path d="M239,328 L247,328 L243,336 Z M319,328 L327,328 L323,336 Z" fill="var(--orange)"/>
    </svg>
    <div class="box flow flow--top ink" style="left:30px;top:216px;width:114px;height:79px;background:var(--yellow)">Claim processed correctly as in network provider. Medical records printed and sent for medical necessity.</div>
    <div class="box flow flow--top ink" style="left:223px;top:216px;width:114px;height:79px;background:var(--orange)">Claim processed out of network. Contact with carrier shows claim processed as out of network in error.<br><br><em>Will representative send the claim back for review?</em></div>
    <div class="box flow flow--small ink" style="left:20px;top:339px;width:50px;height:80px;background:var(--yellow);padding-top:14px">Appeal denied as services were not emergent. Balance is patient responsibility</div>
    <div class="box flow flow--small ink" style="left:105px;top:339px;width:52px;height:80px;background:var(--yellow)">Appeal for claim paid.</div>
    <div class="box flow flow--small ink" style="left:212px;top:339px;width:51px;height:80px;background:var(--orange)">Claim has been sent back for review. Follow up in 14 days.</div>
    <div class="box flow flow--small ink" style="left:298px;top:339px;width:52px;height:80px;background:var(--orange);padding-top:12px">Representative will not send the claim back for review. Appeal sent to carrier. Follow up in 30 days.</div>
    <svg class="corner" viewBox="0 0 46 38"><polygon points="46,0 46,38 0,38" fill="var(--yellow)"/><line x1="40" y1="6" x2="4" y2="36" stroke="#fff" stroke-width="1.5"/></svg>
  </section>

  <!-- Authorization notes -->
  <section class="page" style="left:794px;top:42px">
    <div class="texture" role="img" aria-label="Faint grey geometric background"></div>
    <div class="page-title" style="color:var(--yellow)">Authorization/referral needed.</div>
    <div class="title-bar" style="background:var(--yellow)"></div>
    <div class="notes" style="left:68px;top:130px;width:210px">
      <ol>
        <li>If you are a network provider verify that the claim processed correctly in network. If claim processed out of network have the claim sent back to process or send appeal stating that claim processed incorrectly out of network.</li>
        <li>If you are not a network provider you may send an appeal with medical records attached stating to reprocess and pay claim based on medical necessity.</li>
      </ol>
      <p style="margin-top:8px;padding-left:9px"><b>NOTES ON ACCOUNT SHOULD INCLUDE:</b></p>
      <p style="margin-top:8px;padding-left:9px">- Claim number<br>- Denial date<br>- Processed in or out of network</p>
    </div>
    <svg class="corner" viewBox="0 0 46 38"><polygon points="46,0 46,38 0,38" fill="var(--yellow)"/><line x1="40" y1="6" x2="4" y2="36" stroke="#fff" stroke-width="1.5"/></svg>
  </section>

  <!-- Coding flow -->
  <section class="page" style="left:222px;top:531px">
    <div class="texture" role="img" aria-label="Faint grey geometric background"></div>
    <div class="header header--pink"><strong>Coding Denial</strong><span>CPT/DX/Modifier</span></div>
    <div class="box contact" style="background:var(--pink);font-size:9.5px">Contact made with carrier.</div>
    <svg class="connectors" viewBox="0 0 365 472" fill="none">
      <g stroke="var(--pink)" stroke-width="0.8">
        <polyline points="182,185 182,196"/>
        <polyline points="82,212 82,196 281,196 281,212"/>
      </g>
      <path d="M80,210 L84,210 L82,214 Z M279,210 L283,210 L281,214 Z" fill="var(--pink)"/>
      <g stroke="var(--red)" stroke-width="1.3"><line x1="242" y1="298" x2="242" y2="333"/><line x1="322" y1="298" x2="322" y2="333"/></g>
      <path d="M238,329 L246,329 L242,337 Z M318,329 L326,329 L322,337 Z" fill="var(--red)"/>
    </svg>
    <div class="box flow" style="left:29px;top:218px;width:114px;height:78px;background:var(--pink)">Claim denied in error and has been sent back to process.</div>
    <div class="box flow" style="left:222px;top:218px;width:114px;height:78px;background:var(--red)">Claim denied correctly for coding error</div>
    <div class="box flow flow--small" style="left:210px;top:339px;width:52px;height:80px;background:var(--red)">Forwarded to physician for review</div>
    <div class="box flow flow--small" style="left:297px;top:339px;width:51px;height:80px;background:var(--red)">Corrected and rebilled as a corrected claim</div>
    <svg class="corner" viewBox="0 0 46 38"><polygon points="46,0 46,38 0,38" fill="var(--pink)"/><line x1="40" y1="6" x2="4" y2="36" stroke="#fff" stroke-width="1.5"/></svg>
  </section>

  <!-- Coding notes -->
  <section class="page" style="left:599px;top:531px">
    <div class="texture" role="img" aria-label="Faint grey geometric background"></div>
    <div class="page-title" style="color:var(--pink)">Coding Denial</div>
    <div class="title-bar" style="background:var(--pink)"></div>
    <div class="notes" style="left:96px;top:134px;width:200px">
      <p><b>Example:</b><br>*Claim denied as procedure code used 99203 is for a new patient and this is an established patient.</p>
      <p style="margin-top:7px"><b>ACCOUNT NOTE WILL INCLUDE:</b><br>
      * How information was obtained<br>* Name a representative<br>* Claim number<br>* Denial date<br>* What was denied: CPT, HCPCS, modifier, diagnosis?<br>* What code denied?<br>* Why was it denied?<br>A. Not covered?<br>B. Bundled to another code on the claim? Which code is it bundled with?<br>C. Not a covered benefit per patient policy? Why? What is the service?<br>D. Invalid modifier? What modifier was billed? What is needed?<br>G. Diagnosis does not match CPT? Verify codes billed do not relate to each other.<br>*Appeal address<br>*Timely filing</p>
      <p style="margin-top:14px"><b>*Verify that the claim was billed with the CPT code stated.</b></p>
    </div>
    <svg class="corner" viewBox="0 0 46 38"><polygon points="46,0 46,38 0,38" fill="var(--pink)"/><line x1="40" y1="6" x2="4" y2="36" stroke="#fff" stroke-width="1.5"/></svg>
  </section>

</div>
</body>
</html>
```